Bref créative
Postcard – Double sided - Fun project for awnings
Every shade, storm, breeze and insect guard is built its own way®
Congratulations on the purchase of your new home. We install all types of RETRACTABLE sun, wind.....
Home and Garden
NEW homeowners in the South Florida area. We will mail only single family homes. No condominiums will be mailed to.
The proposed designs should be very creative, unique, clean, modern and “state of the art”
Postcard will be 6” x 11”, high gloss UV coating full color on the front side and black and white on the other side and will need the permit number information in the top right hand corner. Permit information to be provided to the winner.
THE MOST IMPORTANT FACTOR IN THE DESIGN IS THIS......
SINCE OUR PRODUCT IS NOT A PRODUCT THAT MOST DECIDE ON IMMEDIATELY THE POSTCARD SHOULD BE DESIGNED IN A WAY THAT PEOPLE WANT TO KEEP THE POSTCARD SO THAT WHEN THEY ARE READY TO ORDER THEY WILL REMEMBER THE POSTCARD AND OUR COMPANY NAME. OF COURSE IT WILL BE GREAT IF THEY PURCHASE IMMEDIATELY TOO
Postcard will be purchased here: http://www.prismaveto.com/A_post_cards.php
Specifications for postcard upload are at these links: http://www.prismaveto.com/A_product_requirements.php
http://www.prismaveto.com/upform.php
Post office layout requirements are at the link below. The design MUST meet these exact specifications or the postcards cannot be mailed.
http://pe.mailrelaynet.com/text/qsg300/Q602.htm
Benefits of our products are below. I would also recommend reading the homepage http://www.foldcanopyworks.com/ for more information and benefits.
1. All types and all models are retractable prior to high winds or hurricanes
2. Adds new life to a patio, deck, terrace, balcony, poolside or Jacuzzi
3. Durafinex® powder coated frames. Won’t peel or chip
4. Keeps out heat and lowers your electric bill
5. Retains room brightness and protects indoor furnishings
6. Decreases glare and UV rays but not the view. Heat gain reduced by 77%
7. Retractable on cloudy days for interior room brightness
8. Highest quality heavy duty non-rusting aluminum with non-rusting Vemba stainless steel components
9. 25 year frame warranty
10. CE and KLÖR certified frames and Italian Lumo fabrics
Product information links for each model type are below. All models are retractable
1. Lateral folding arm awnings http://www.foldcanopyworks.com/lateral-arm-awnings/velorin-plus.html
2. Retractable patio cover systems http://www.foldcanopyworks.com/patio-cover-awnings/belmadro.html
3. Vertical drop awnings http://www.foldcanopyworks.com/drop-down-awnings/quiva.html
4. Canopy awnings http://www.foldcanopyworks.com/canopy-awnings/vendrillo.html
5. Side arm awnings http://www.foldcanopyworks.com/side-arm-drop-arm-awnings/molvane.html
6. Free standing awning http://www.foldcanopyworks.com/free-standing-awnings/gastelo.html
All projects can be motorized using a remote control, wall switch, timer or temperature sensor.
We offer wind, sun and rain sensors
Retractable patio cover system
Lateral folding arm awning
Vertical drop awning
Side Arm Awning
Canopy awning
Free standing awning
Logo to be uploaded.

```html
<!DOCTYPE html>
<html lang="en">
<head>
<meta charset="utf-8">
<title>Awning Postcards – Front and Back</title>
<link rel="stylesheet" href="https://fonts.googleapis.com/css2?family=Open+Sans:wght@400;600;700;800&family=Great+Vibes&display=swap">
<style>
:root{
  --stage:#7a5535;
  --navy:#10306a;
  --blue:#1d5fb1;
  --sky:#4a9be0;
  --pale:#dcebf8;
  --orange:#f08a24;
  --white:#ffffff;
  --ink:#1f2a3a;
  --muted:#5d6a7c;
  --label:#f3ead8;
}
*{box-sizing:border-box;margin:0;padding:0}
html,body{width:1200px;height:461px;overflow:hidden}
body{background:var(--stage);font-family:"Open Sans",Arial,sans-serif;color:var(--ink);position:relative}
.column{position:absolute;top:0;width:384px;height:461px}
.col-a{left:8px}.col-b{left:408px}.col-c{left:808px}
.side-label{position:absolute;left:2px;font-size:11px;font-weight:700;color:var(--label)}
.label-front{top:11px}.label-back{top:232px}
.card{position:absolute;left:0;width:384px;height:192px;background:var(--white);overflow:hidden;box-shadow:0 2px 6px rgba(0,0,0,.45)}
.card-front{top:28px}.card-back{top:251px}
.card svg.shape{position:absolute;inset:0;width:100%;height:100%}
.brand{position:absolute;display:flex;align-items:center;gap:5px;font-weight:800;color:var(--navy);font-size:11px}
.brand .dot{width:14px;height:14px;border-radius:50%;background:var(--orange)}
.brand-sub{position:absolute;font-size:5px;line-height:1.35;color:var(--muted)}
.greeting{position:absolute;font-family:"Great Vibes",cursive;font-size:22px;color:var(--navy)}
.photo{position:absolute}
.offer{position:absolute;color:var(--white);text-align:right;font-weight:700;line-height:1.15}
.offer .lead{font-size:9px;letter-spacing:.5px}
.offer .line{font-size:6px;font-weight:600}
.permit{position:absolute;top:8px;right:8px;width:44px;height:26px;border:1px solid var(--ink);font-size:4.5px;text-align:center;padding-top:4px;line-height:1.3}
.small-text{position:absolute;font-size:4.6px;line-height:1.45;color:var(--ink)}
.list{position:absolute;list-style:none;font-size:4.6px;line-height:1.55;color:var(--white)}
.list li::before{content:"› ";color:var(--orange);font-weight:700}
.list.dark{color:var(--ink)}
.section-title{position:absolute;font-weight:800;color:var(--white);font-size:11px}
.bar-title{position:absolute;background:var(--blue);color:var(--white);font-size:7px;font-weight:700;padding:3px 6px}
.cta{position:absolute;color:var(--white);font-weight:700;font-size:7px}
.address{position:absolute;font-size:5px;line-height:1.5;color:var(--ink)}
</style>
</head>
<body>

<!-- Design A -->
<section class="column col-a">
  <p class="side-label label-front">Front</p>
  <article class="card card-front">
    <div class="photo" role="img" aria-label="Patio with retractable awning and parked car" style="left:0;top:44px;width:384px;height:110px;background:linear-gradient(180deg,#a9c7df,#6d7f8f 60%,#3d4650)"></div>
    <svg class="shape" viewBox="0 0 384 192" preserveAspectRatio="none">
      <path d="M0 150 C120 120 250 125 384 140 L384 192 L0 192Z" fill="var(--navy)"/>
      <path d="M0 150 C120 120 250 125 384 140 L384 146 C250 132 120 128 0 158Z" fill="var(--sky)"/>
    </svg>
    <div class="brand" style="left:10px;top:10px"><span class="dot"></span>Foldcanopyworks.com</div>
    <p class="brand-sub" style="left:29px;top:25px">(305) 555-0148</p>
    <p class="greeting" style="right:12px;top:4px">Congratulations</p>
    <div class="offer" style="right:12px;top:164px"><div class="lead">WE OFFER</div><div class="line">WIND, SUN AND RAIN SENSORS</div></div>
  </article>

  <p class="side-label label-back">Back</p>
  <article class="card card-back">
    <svg class="shape" viewBox="0 0 384 192" preserveAspectRatio="none">
      <path d="M0 0 L170 0 C195 60 150 130 185 192 L0 192Z" fill="var(--blue)"/>
      <path d="M170 0 C195 60 150 130 185 192 L178 192 C143 130 188 60 163 0Z" fill="var(--sky)"/>
    </svg>
    <h2 class="section-title" style="left:10px;top:10px">SERVICES</h2>
    <ul class="list" style="left:10px;top:28px;width:150px">
      <li>All types and models retract before high winds</li>
      <li>Adds new life to a patio, deck or poolside</li>
      <li>Durafinex® powder coated frames</li>
      <li>Keeps out heat, lowers your electric bill</li>
      <li>Retains room brightness, protects furnishings</li>
      <li>Decreases glare and UV rays but not the view</li>
      <li>Non-rusting aluminum, Vemba stainless parts</li>
      <li>25 year frame warranty</li>
      <li>CE and KLÖR certified frames, Lumo fabrics</li>
      <li>Motorized by remote, switch, timer or sensor</li>
    </ul>
    <div class="permit">PRSRT STD<br>U.S. POSTAGE<br>PAID</div>
    <p class="address" style="left:220px;top:80px">Current Resident<br>Street address line<br>City, State ZIP</p>
    <div class="brand" style="left:200px;top:160px"><span class="dot"></span>Foldcanopyworks.com</div>
    <p class="brand-sub" style="left:219px;top:175px">1400 Seaview Ave, Coral Bay FL 33000</p>
  </article>
</section>

<!-- Design B -->
<section class="column col-b">
  <p class="side-label label-front">Front</p>
  <article class="card card-front">
    <svg class="shape" viewBox="0 0 384 192" preserveAspectRatio="none">
      <rect width="384" height="192" fill="var(--navy)"/>
      <path d="M0 0 L384 0 L384 40 C250 50 120 40 0 55Z" fill="var(--white)"/>
    </svg>
    <div class="photo" role="img" aria-label="Blue retractable awning over a terrace" style="left:130px;top:40px;width:254px;height:118px;background:linear-gradient(160deg,#3e78c0,#9cc0e2 55%,#c7b79a)"></div>
    <svg class="shape" viewBox="0 0 384 192" preserveAspectRatio="none">
      <path d="M0 150 C130 130 260 140 384 160 L384 192 L0 192Z" fill="var(--blue)"/>
      <path d="M0 150 C130 130 260 140 384 160 L384 165 C260 146 130 136 0 156Z" fill="var(--sky)"/>
    </svg>
    <div class="brand" style="left:10px;top:10px"><span class="dot"></span>Foldcanopyworks.com</div>
    <p class="brand-sub" style="left:29px;top:25px">(305) 555-0148</p>
    <p class="greeting" style="right:12px;top:4px">Congratulations</p>
    <p class="small-text" style="left:10px;top:62px;width:112px;color:var(--pale)">Every shade, storm, breeze and insect guard is built its own way®</p>
    <div class="offer" style="right:12px;top:168px"><div class="lead">WE OFFER</div><div class="line">WIND, SUN AND RAIN SENSORS</div></div>
  </article>

  <p class="side-label label-back">Back</p>
  <article class="card card-back">
    <div class="photo" role="img" aria-label="Lateral arm awning over a patio" style="left:10px;top:8px;width:110px;height:60px;background:linear-gradient(180deg,#9ec4e6,#6b8aa6)"></div>
    <div class="bar-title" style="left:10px;top:74px;width:190px">Velorin PLUS – Traditional awning</div>
    <ul class="list dark" style="left:12px;top:92px;width:190px">
      <li>Lateral folding arm awning, fully retractable</li>
      <li>Adds new life to a deck, terrace or balcony</li>
      <li>Heat gain reduced by 77%</li>
      <li>Retractable on cloudy days for brightness</li>
      <li>Heavy duty non-rusting aluminum frame</li>
      <li>25 year frame warranty</li>
      <li>Motorized with remote control or sensor</li>
    </ul>
    <div class="permit">PRSRT STD<br>U.S. POSTAGE<br>PAID</div>
    <p class="address" style="left:235px;top:80px">Current Resident<br>Street address line<br>City, State ZIP</p>
    <div class="brand" style="left:10px;top:170px;font-size:9px"><span class="dot" style="width:11px;height:11px"></span>Foldcanopyworks.com</div>
  </article>
</section>

<!-- Design C -->
<section class="column col-c">
  <p class="side-label label-front">Front</p>
  <article class="card card-front">
    <svg class="shape" viewBox="0 0 384 192" preserveAspectRatio="none">
      <path d="M200 0 L384 0 L384 40 L215 40 C205 25 205 12 200 0Z" fill="var(--orange)"/>
      <path d="M0 95 L150 95 C185 95 195 140 175 192 L0 192Z" fill="var(--blue)"/>
    </svg>
    <div class="photo" role="img" aria-label="Retractable patio cover over an outdoor lounge" style="left:176px;top:42px;width:208px;height:150px;background:linear-gradient(180deg,#e7e1d3,#b9a98c 60%,#6f6a5d)"></div>
    <div class="brand" style="left:10px;top:14px"><span class="dot"></span>Foldcanopyworks.com</div>
    <p class="greeting" style="right:12px;top:6px;color:var(--white)">Congratulations</p>
    <p class="cta" style="left:10px;top:108px;width:150px;font-size:8px;line-height:1.3">Call The Retractable Awning &amp; Patio Cover Experts</p>
    <p class="small-text" style="left:10px;top:140px;width:150px;color:var(--pale)">(305) 555-0148<br>www.foldcanopyworks.com<br>Serving new homeowners in South Florida</p>
  </article>

  <p class="side-label label-back">Back</p>
  <article class="card card-back">
    <svg class="shape" viewBox="0 0 384 192" preserveAspectRatio="none">
      <rect x="0" y="168" width="384" height="24" fill="var(--blue)"/>
      <rect x="0" y="164" width="384" height="4" fill="var(--orange)"/>
    </svg>
    <div class="bar-title" style="left:8px;top:8px;width:230px">Belmadro – Attached Retractable Patio Cover System</div>
    <p class="small-text" style="left:8px;top:26px;width:230px">Retractable patio cover systems add shade to any patio, deck or poolside. All models retract prior to high winds or hurricanes and keep out heat.</p>
    <div class="photo" role="img" aria-label="Attached patio cover system" style="left:8px;top:58px;width:100px;height:70px;background:linear-gradient(180deg,#d8dde2,#8d98a3)"></div>
    <ul class="list dark" style="left:114px;top:60px;width:130px">
      <li>Durafinex® powder coated frames</li>
      <li>Lowers your electric bill</li>
      <li>Protects indoor furnishings</li>
      <li>25 year frame warranty</li>
      <li>Wind, sun and rain sensors</li>
    </ul>
    <div class="permit">PRSRT STD<br>U.S. POSTAGE<br>PAID</div>
    <p class="address" style="left:260px;top:80px">Current Resident<br>Street address line<br>City, State ZIP</p>
    <p class="cta" style="left:10px;top:176px">Call The Retractable Awning &amp; Patio Cover Experts</p>
    <p class="cta" style="right:10px;top:176px">(305) 555-0148</p>
  </article>
</section>

</body>
</html>
```